Web Design Accounting-Tax and related business service online.

We are looking to develop a website/online application for users in the South African market to register and buy Accounting/tax and related services online. (New business registrations/Income tax returns/Payroll) etc

The Domain will be www.ledgerbright-hub.co.za and the business will be run under Valkmere Financial Services.

The domain - www.ledgerbright-hub.co.za will be used as the "trading" name of the site, so any sections that possible make use name use domain name.

We are looking for designs for the website.

Here is the requirements as from the developer

• Home Page: Design of the home page of the website.
• Forms: We have different forms in the application. Need any one form designed. Just look and feel without functionality.
• Member Area: when a user will log in, the layout of dashboard to show them.

UPDATE (Previously HTML required) - Can be in PSD format for this Contest.

(If you prepared/capable to handle the PSD to HTML conversation you can quote seperate for this)

Websites that offer similar services (Not for design inspiration please, but idea of possible website layout etc)

http://www.quillpenny-direct.co.za/
http://www.venturefile-desk.co.za/

See our current static website for colour schemes that I like.

www.valkmere.co.za

Prefer clean, modern - uncluttered look.

Target Market(s)

Users that pefer employing tech and ease of obtaining services online to having Accountant physically close.

Industry/Entity Type

Business Service

Requirements
Must have
• Clean, Modern, uncluttered look.

Nice to have

Should not have
• Old "boring" stiff accounting designs. No clutter or too busy.

```html
<!DOCTYPE html>
<html lang="en">
<head>
<meta charset="utf-8">
<title>Valkmere Financial Services – Online accounting and tax</title>
<link href="https://fonts.googleapis.com/css2?family=Arimo:wght@400;700&family=Tinos:ital@1&family=Open+Sans:ital,wght@1,700&display=swap" rel="stylesheet">
<style>
:root{
  --teal:#0e6a6e;--teal-dark:#0a4f52;--green:#2f7a33;--green-light:#4a9a3c;
  --grey-bg:#e6e6e6;--panel:#dcdcdc;--ink:#444;--ink-dark:#222;--black:#111;
  --menu:#e9e9e9;--menu-line:#c8c8c8;--red:#7a1a12;--link:#1a4f8a;
}
*{box-sizing:border-box;margin:0;padding:0}
html,body{width:973px;height:1200px;overflow:hidden;background:#fff}
body{position:relative;font-family:Arimo,Arial,sans-serif;color:var(--ink);font-size:11px}
.abs{position:absolute}
.header{left:0;top:0;width:973px;height:86px;background:linear-gradient(#f4f4f4,#dedede)}
.brand{left:140px;top:32px;display:flex;align-items:center;gap:10px}
.brand-dot{width:44px;height:44px;border-radius:50%;background:var(--green-light)}
.brand-name{font-size:17px;font-weight:700;color:var(--teal-dark);line-height:1.1}
.brand-name small{display:block;font-size:9px;font-weight:400;color:var(--ink)}
.search{left:681px;top:4px;display:flex;gap:4px}
.search input{width:88px;height:20px;border:1px solid #bbb;font:italic 9px Arimo,sans-serif;padding-left:4px;color:#666}
.search button{width:52px;height:22px;background:var(--green);color:#fff;border:1px solid #1d5a22;font:700 11px Arimo,sans-serif}
.social{top:40px;width:28px;height:30px;background:#7a8c99;border-radius:3px}
.nav{left:0;top:86px;width:973px;height:62px;background:linear-gradient(var(--teal),var(--teal-dark));border-top:4px solid #1d8a8a}
.nav a{position:absolute;top:22px;color:#fff;font-size:9px;font-weight:700;text-decoration:none}
.sitemap{left:802px;top:128px;color:#fff;font-size:11px;text-decoration:underline}
.banner{left:0;top:148px;width:973px;height:89px;background:linear-gradient(#2b6f2f,#3e8a3c 60%,#2b6f2f)}
.banner-art{left:125px;top:180px;width:135px;height:26px;background:linear-gradient(90deg,rgba(143,195,232,.05),rgba(143,195,232,.35),rgba(143,195,232,.05));border-radius:3px}
.tagline{left:264px;top:176px;font:italic 700 20px "Open Sans",sans-serif;color:#fff}
.tagline-mirror{left:264px;top:202px;font:italic 700 20px "Open Sans",sans-serif;color:#fff;opacity:.18;transform:scaleY(-1)}
.gap{left:0;top:237px;width:973px;height:44px;background:linear-gradient(#f6f6f6,#e4e4e4)}
.crumb{left:124px;top:264px;font-size:8px;color:#999}
.crumb b{color:#555}
.side-menu{left:151px;top:309px;width:157px;list-style:none}
.side-menu li{height:18.5px;line-height:17px;padding-left:20px;background:var(--menu);border:1px solid var(--menu-line);border-top:none;font-size:10.5px;color:#555;position:relative}
.side-menu li::before{content:"";position:absolute;left:7px;top:6px;width:5px;height:5px;border-radius:50%;background:#aaa}
.faq-badge{left:152px;top:600px;width:70px;height:70px;border-radius:50%;background:radial-gradient(circle at 40% 35%,#4d8fd8,#1a4f9a)}
.q{left:160px;width:148px;background:var(--menu);border:1px solid var(--menu-line);font-weight:700;font-size:11px;color:#333;padding:3px 6px 3px 20px;line-height:13px}
.a{left:148px;width:162px;border-left:3px solid #222;padding-left:8px;font:italic 10px/14px Tinos,serif;color:#333}
.main{left:338px;top:306px;width:270px;font-size:10.5px;line-height:15.5px;color:#555}
.main p{margin-bottom:14px}
.main .drop{font-size:15px;font-weight:700;color:#222}
.main h2{font-size:15px;font-weight:400;color:#333;margin-bottom:6px}
.main h3{font-size:10.5px;font-weight:700;color:#333;margin:0 0 14px 6px}
.partner-img{float:right;width:80px;height:92px;margin:-18px 0 4px 8px;background:linear-gradient(#f2f2f2,#b9bfc4)}
.main a{color:var(--link)}
.panel-h{left:637px;width:208px;height:22px;color:#fff;font-size:10px;font-weight:700;padding:6px 10px}
.panel{left:637px;width:208px;background:var(--panel);font-size:10.5px;line-height:15px;color:#555;padding:4px 6px}
.chart-img{float:right;width:104px;height:86px;margin:22px 0 4px 4px;background:linear-gradient(135deg,#f4f6f8,#8aa3b8)}
.signup{left:658px;top:542px;width:82px;height:19px;background:linear-gradient(#2a7a2e,#123f17);color:#fff;font-size:13px;font-weight:700;text-align:center;line-height:19px}
.steps li{list-style:none;padding-left:16px;position:relative}
.steps li::before{content:"";position:absolute;left:2px;top:4px;width:8px;height:7px;background:#8a6a1a;border-radius:50%}
.entry label{position:absolute;font-size:10.5px;color:#444}
.entry input{position:absolute;width:72px;height:16px;border:1px solid #7aa;background:#fff}
.entry .lnk{position:absolute;font-size:9px;font-weight:700;color:#333}
.login{left:655px;top:1052px;width:30px;height:16px;border:1px solid #999;background:#f3f3f3;font-size:9px;text-align:center;line-height:14px}
.foot-links a{position:absolute;top:1144px;font-size:10.5px;font-weight:700;color:#111;text-decoration:underline}
.foot-dot{left:748px;top:1124px;width:52px;height:52px;border-radius:50%;background:radial-gradient(circle at 40% 35%,#8fd17a,#2f7a33);border:3px solid #fff;box-shadow:0 0 2px #888}
.strip{left:118px;top:1165px;width:735px;height:8px;background:var(--red)}
.bar{left:118px;top:1173px;width:855px;height:27px;background:var(--black);color:#ddd;font-size:8px;padding:9px 0 0 475px}
.bar b{color:#fff;text-decoration:underline}
</style>
</head>
<body>
<div class="abs header"></div>
<div class="abs brand"><span class="brand-dot"></span><span class="brand-name">Valkmere<small>Financial Services CC<br>CK 2010/000000/23</small></span></div>
<form class="abs search"><input value="enter keyword here"><button type="button">Search</button></form>
<span class="abs social" style="left:677px"></span>
<span class="abs social" style="left:719px"></span>
<span class="abs social" style="left:763px"></span>
<span class="abs social" style="left:807px"></span>

<nav class="abs nav">
  <a style="left:130px">HOME</a><a style="left:185px">ABOUT US ▾</a><a style="left:270px">SERVICES ▾</a><a style="left:351px">FEES</a><a style="left:400px">REGISTER</a><a style="left:471px">FAQ</a><a style="left:518px">PORTFOLIO</a><a style="left:595px">CONTACT</a>
</nav>
<div class="abs banner"></div>
<div class="abs banner-art" role="img" aria-label="Sketched mountain line decoration"></div>
<a class="abs sitemap">site map</a>
<div class="abs tagline">Online accounting and tax solutions @ your finger tip</div>
<div class="abs tagline-mirror" aria-hidden="true">Online accounting and tax solutions @ your finger tip</div>
<div class="abs gap"></div>
<div class="abs crumb">You are here: <b>Home</b></div>

<ul class="abs side-menu" style="border-top:1px solid var(--menu-line)">
  <li>Tax Returns</li><li>Tax Registration</li><li>Accounting Packages</li><li>Company Registration</li><li>Financial Reports</li><li>Financial Analysis</li><li>Tax Clearance Certificates</li><li>Annual Registry Returns</li><li>Import/Export Licenses</li><li>Trust Registrations.</li><li>BookKeeping Services</li><li>Payrol/Payslip Processing</li><li>UIF Registration/Services</li><li>Trust Registrations</li>
</ul>
<div class="abs faq-badge"></div>
<div class="abs q" style="top:693px">Who qualifies to be a director?</div>
<div class="abs a" style="top:751px">A director is one who runs a company. He may not necessary be a shareholder but most times do.</div>
<div class="abs q" style="top:832px">How long does it take to precess my company registration?</div>
<div class="abs a" style="top:893px">If all the necessary documents are supplies on time, it could take between 7 and 14 day. After scuting by us, the application is then forwarded to Revenue Office for approval</div>

<main class="abs main">
  <p><span class="drop">W</span>e believe in providing you with all the financial services, tools and support you need to move from surviving (or not) to prosper at competitive rates!</p>
  <p>We specialize in providing solutions for startup companies to medium enterprises to help you comply with all statutory requirements as well as provide you with the means to measure performance and make the right choice based on these figures.</p>
  <p>So contact us today for a FREE assessment of your requirements and we will tailor a solution to your budget!</p>
  <h2>Why become a partner?</h2>
  <p><span class="partner-img" role="img" aria-label="Two business figures shaking hands"></span>A Partner is a person who can render a service/product through our site. We will consider adding your service/products for sale through our site provided:</p>
  <p>• The service/products are business-related</p>
  <p>• You, as the Service Provider, own all rights in and to the service/product</p>
  <p>• The service meets our approval.</p>
  <p>• We are satisfied with your credentials.</p>
  <h3>What are the Benefits of being a Partner?</h3>
  <p>A Partner is able to provide procuts/services via our site, without having to worry about the associated website costs and marketing. A Partner earns a % (dependent of the type of service, which will be discussed upon your application)of the total sale price of each of the product/services that are sold via our site. We bear any marketing, commission and other costs associated with the sale!</p>
  <h2>Valkmere Forum</h2>
  <p>Join our forum and interract with other clients and users. Benefit from others experiences and also contribute in &nbsp;<a>our forum</a></p>
</main>

<div class="abs panel-h" style="top:307px;background:var(--black)">ACOUNTING SOLUTIONS</div>
<div class="abs panel" style="top:329px;height:242px"><span class="chart-img" role="img" aria-label="Financial charts and graphs"></span>We offer a comprehensive range of business and accounting solutions to our clients specifically design and customisable to your personal or corporate accounting needs. We also offer consultancy and registrations services on Tax matters including Company Registry registrations and all Revenue Office registrations.</div>
<div class="abs signup">Sign Up</div>

<div class="abs panel-h" style="top:588px;background:var(--green-light)">SIMPLE STEPS TO FOLLOW</div>
<div class="abs panel" style="top:610px;height:293px">There are just few simple steps to foolow to get full value of any of our services. Let's break it down to these . .
  <ul class="steps">
    <li>- Browse the site for our range of available services</li>
    <li>- Register by signing up for free</li>
    <li>- Follow the simple instructions for your specific needs.</li>
    <li>- Pay via secure online payment (if applicable).</li>
    <li>- Acknowledgement of receipt of payment and relevant information on required documentation will be sent to you via email.</li>
    <li>- You will be updated with periodic progressof your transactions via email and SMS</li>
  </ul>
</div>

<div class="abs panel-h" style="top:918px;background:var(--black)">ENTRY</div>
<div class="abs panel entry" style="top:940px;height:134px">
  <label style="left:72px;top:13px">Login:</label><input style="left:122px;top:12px">
  <label style="left:55px;top:36px">Password:</label><input style="left:122px;top:35px">
  <span class="lnk" style="left:33px;top:76px">REGISTRATION</span>
  <span class="lnk" style="left:128px;top:70px;line-height:13px">FORGOT<br>PASSWORD?</span>
</div>
<div class="abs login">Login</div>

<svg class="abs" style="left:118px;top:1115px" width="735" height="14" viewBox="0 0 735 14"><path d="M0,2 Q0,10 12,10 H723 Q735,10 735,2" fill="none" stroke="#bbb" stroke-width="2"/></svg>
<div class="foot-links">
  <a style="left:154px">About Us</a><a style="left:281px">Registration</a><a style="left:437px">FAQ</a><a style="left:558px">Site Map</a><a style="left:687px">Contact Us</a>
</div>
<div class="abs strip"></div>
<div class="abs bar">© www.valkmere.co.za 2010. | Powered by &nbsp;<b>brightloom studio</b></div>
<div class="abs foot-dot"></div>
</body>
</html>
```